Real Estate Company Looking for Business Card Designs for 3 Executives

Hello!
Thanks so much for considering our project! We are a real estate investment company located in Edmonton, Alberta called Bellcrane Group of Companies. We invest/develop both commercial and residential real estate and are looking to create 3 DOUBLE-SIDED business cards for 3 top executives in the company! (for some reason it won't let us select the double-sided option, but yes, the cards are double sided and would be happy to tip extra)

We have certain guidelines that we want our business cards to for sure follow - the back of the Business card has to be the Black Background Version of the Logo which has already been designed and linked as a file (first file). We want the entire back of the card to simply just be the black background logo. In terms of the front of the card, would like to see a smaller version of the white background logo (linked as the second file) in the top left hand corner - of course, feel free to get creative and we can make revisions together along the way! and Then after that, just text. We want the card to be sharp, clean, easy on the eyes and highly professional looking. We would like the card to include the Full name of the Company (Bellcrane Group of Companies), Name of the Person, Title, Phone, Email. If possible please provide the front part of the card for 3 people:

1) Bellcrane Group of Companies, Nora Lindqvist, Chief Financial Officer, 780-555-0142, noralindqvist@bellcranegroup.example

2) Bellcrane Group of Companies, Julien Lindqvist, Chief Executive Officer, 780-555-0187, julienlindqvist@bellcranegroup.example

3) Bellcrane Group of Companies, Tom Okafor, Chief Operations Officer, 587-555-0163, tomokafor@bellcranegroup.example

Thank you so much for considering our project & we look forward to seeing your designs!

```html
<!DOCTYPE html>
<html lang="en">
<head>
<meta charset="utf-8">
<title>Bellcrane Business Card</title>
<link rel="stylesheet" href="https://fonts.googleapis.com/css2?family=Jost:wght@400;500;600&family=Libre+Caslon+Text:wght@700&display=swap">
<style>
  :root {
    --stage: #a9a9a9;
    --card-black: #070304;
    --card-white: #ffffff;
    --ink: #111111;
    --muted: #6b6b6b;
    --icon: #9a9a9a;
    --tree-tone: #e2e2e2;
  }
  * { margin: 0; padding: 0; box-sizing: border-box; }
  html, body {
    width: 1200px; height: 1000px; overflow: hidden;
    background: var(--stage);
    font-family: "Jost", sans-serif;
  }
  .stage { position: relative; width: 1200px; height: 1000px; }
  .card {
    position: absolute; left: 294px; width: 613px; height: 351px;
    border-radius: 22px; overflow: hidden;
    box-shadow: 0 22px 40px rgba(0,0,0,0.28);
  }
  .card-back { top: 82px; background: var(--card-black); }
  .card-front { top: 545px; background: var(--card-white); }

  .brand-name {
    position: absolute; font-family: "Jost", sans-serif; font-weight: 500;
    text-transform: uppercase; white-space: nowrap;
  }
  .card-back .brand-name {
    left: 0; right: 0; top: 122px; text-align: center;
    color: var(--card-white); font-size: 42px; letter-spacing: 9px;
    padding-left: 9px;
  }
  .card-front .brand-name {
    left: 37px; top: 44px; color: var(--ink);
    font-size: 16px; letter-spacing: 2.4px;
  }
  .company-name {
    position: absolute; left: 205px; top: 60px;
    font-size: 14.5px; font-weight: 600; letter-spacing: 2.6px;
    color: var(--ink); text-transform: uppercase; white-space: nowrap;
  }
  .tree-art {
    position: absolute; right: 0; top: 0; width: 122px; height: 351px;
    background: linear-gradient(90deg, rgba(226,226,226,0) 0%, var(--tree-tone) 35%, var(--tree-tone) 65%, rgba(226,226,226,0.4) 100%);
    opacity: 0.7;
  }
  .person-name {
    position: absolute; left: 53px; top: 162px;
    font-family: "Libre Caslon Text", serif; font-weight: 700;
    font-size: 33px; color: var(--ink); white-space: nowrap;
  }
  .person-title {
    position: absolute; left: 53px; top: 205px;
    font-size: 14.5px; letter-spacing: 1.3px; color: var(--muted);
    text-transform: uppercase; white-space: nowrap;
  }
  .contact {
    position: absolute; left: 53px; display: flex; align-items: center;
    font-size: 16px; color: var(--ink); white-space: nowrap;
  }
  .contact svg { fill: var(--icon); margin-right: 6px; }
  .contact-phone { top: 251px; }
  .contact-email { top: 280px; }
</style>
</head>
<body>
<main class="stage">
  <section class="card card-back" aria-label="Card back">
    <div class="brand-name">Bellcrane</div>
  </section>

  <section class="card card-front" aria-label="Card front">
    <div class="tree-art" role="img" aria-label="Faint tall tree decoration"></div>
    <div class="brand-name">Bellcrane</div>
    <div class="company-name">Bellcrane Group of Companies</div>
    <h1 class="person-name">Nora Lindqvist</h1>
    <div class="person-title">Chief Financial Officer</div>
    <div class="contact contact-phone">
      <svg width="19" height="19" viewBox="0 0 24 24" aria-hidden="true"><path d="M6.6 10.8a15.1 15.1 0 0 0 6.6 6.6l2.2-2.2c.3-.3.7-.4 1-.2 1.1.4 2.3.6 3.6.6.6 0 1 .4 1 1V20c0 .6-.4 1-1 1A17 17 0 0 1 3 4c0-.6.4-1 1-1h3.5c.6 0 1 .4 1 1 0 1.3.2 2.5.6 3.6.1.3 0 .7-.2 1z"/></svg>
      <span>780-555-0142</span>
    </div>
    <div class="contact contact-email">
      <svg width="22" height="16" viewBox="0 0 22 16" aria-hidden="true"><path d="M0 0h22v16H0z M1.5 1.5v.6L11 9l9.5-6.9v-.6z" fill-rule="evenodd"/><path d="M1.5 3.5 11 10.5l9.5-7V14.5h-19z" fill="#c4c4c4"/></svg>
      <span>noralindqvist@bellcranegroup.example</span>
    </div>
  </section>
</main>
</body>
</html>
```